Postcard Design for Direct Mail Campaign for PIttsburgh area attorney

I am an attorney in Pittsburgh, I did this before and selected three designs. I am not sure if those responding can see which three I selected. Those designs are in use now. All 3 go out. The issue is they cost the standard mailing rate and I will use all 3 of those forever. There will be times I would like to take advantage of the postcard mailing rate and thus this one is smaller. I want the postcard to emphasize I do criminal and SOME civil law. See my sites www.brookvaledefenselaw.com and www.tovacounsel.net.

IN FACT I AM PUTTING THE THREE I AM MAILING RIGHT NOW IN THE IMAGES> I TRUST THAT THESE WILL BE USED TO INSPIRE AND GUIDE AND NO COPY. i Cannot upload those images. You can probably see my 3 winners.

Target Market(s)

Pittsburgh area people who may need a criminal attorney or a civil attorney.

Industry/Entity Type

Legal

Colors
ec1f27

Requirements
Must have
• A balanced criminal - civil thing as these are going to people in the mail with no envelope.
Nice to have
• On my site www.brookvaledefenselaw.com I have badges in the sidebar.
Should not have
• People being arrested. I am putting up new images.

```html
<!DOCTYPE html>
<html lang="en">
<head>
<meta charset="utf-8">
<title>Postcard – The Law Office of Daniel R. Castellan</title>
<link rel="stylesheet" href="https://fonts.googleapis.com/css2?family=Cinzel:wght@400;600&family=Montserrat:wght@400&family=Open+Sans:wght@400;700&display=swap">
<style>
  :root{
    --page:#c6c7ca;
    --band:#232525;
    --navy-top:#1d3f86;
    --navy-bottom:#0b1a45;
    --gold:#f3cf5e;
    --muted:#d8dbe6;
    --white:#ffffff;
    --pill:#e6e6e4;
    --ink:#1c1c1c;
  }
  *{margin:0;padding:0;box-sizing:border-box}
  html,body{width:1200px;height:1200px;overflow:hidden}
  body{background:var(--page);position:relative;font-family:"Open Sans",sans-serif}

  .card{position:absolute;left:254px;width:730px;overflow:hidden;box-shadow:0 0 0 1px rgba(0,0,0,.25)}

  /* front */
  .front{top:84px;height:492px;background:linear-gradient(180deg,var(--navy-top) 0%,var(--navy-bottom) 100%)}
  .front-band{position:absolute;inset:0;width:100%;height:100%}
  .title{position:absolute;left:0;width:444px;text-align:center;font-family:"Cinzel",serif;font-weight:400;color:var(--white);font-size:29px;line-height:1;letter-spacing:.5px;white-space:nowrap}
  .title-1{top:27px}
  .title-2{top:63px}
  .subtitle{position:absolute;left:0;width:444px;top:100px;text-align:center;font-family:"Cinzel",serif;color:var(--white);font-size:12.5px;letter-spacing:.3px;white-space:nowrap}
  .appointment{position:absolute;left:450px;width:270px;top:26px;text-align:center;font-family:"Montserrat",sans-serif;color:var(--white);font-size:15px;line-height:18px;white-space:nowrap}
  .phone{position:absolute;left:450px;width:270px;top:46px;text-align:center;font-family:"Montserrat",sans-serif;color:var(--white);font-size:25px;line-height:30px;white-space:nowrap}

  .features{position:absolute;left:25px;top:164px;list-style:none;font-family:"Cinzel",serif}
  .feature{position:relative;padding-left:16px;color:var(--gold);font-size:13.5px;font-weight:600;line-height:16px;margin-bottom:8px}
  .feature::before{content:"";position:absolute;left:0;top:3px;width:10px;height:10px;background:var(--gold);clip-path:polygon(25% 0,75% 0,100% 50%,75% 100%,25% 100%,0 50%)}
  .practice{list-style:none;margin:4px 0 0 14px;color:var(--muted);font-size:12px;font-weight:400;line-height:16px}
  .appeals{list-style:none;margin:4px 0 0 12px;color:var(--muted);font-size:11.5px;font-weight:400;line-height:16px}
  .appeals li::before{content:"• "}
  .photo-cluster{position:absolute;left:480px;top:110px;width:250px;height:284px}

  /* back */
  .back{top:624px;height:494px;background:var(--white)}
  .back-panel{position:absolute;left:0;top:0;width:405px;height:100%;background:linear-gradient(180deg,var(--navy-top) 0%,var(--navy-bottom) 100%)}
  .pill{position:absolute;left:115px;width:190px;height:24px;border-radius:12px;background:var(--pill);color:var(--ink);text-align:center;font-size:15px;line-height:24px}
  .pill-map{top:20px}
  .pill-contact{top:286px}
  .map{position:absolute;left:20px;top:48px;width:382px;height:234px;background:linear-gradient(135deg,#ecebe6 0%,#e2dccb 60%,#d8d3c4 100%)}
  .contact{position:absolute;top:316px;color:var(--white);font-size:14px;line-height:21.6px;font-style:normal;white-space:nowrap}
  .contact-address{left:28px}
  .contact-address .name{font-weight:700}
  .contact-lines{left:208px}
  .contact-lines .indent-phone{padding-left:36px}
  .contact-lines .indent-mail{padding-left:5px}
  .websites{position:absolute;left:0;width:390px;top:428px;text-align:center;color:var(--white);font-size:16px;line-height:22px}
  .stamp{position:absolute;left:584px;top:36px;width:115px;height:77px;border:2px solid #222;display:flex;align-items:center;justify-content:center;font-size:16px;color:var(--ink)}
  .address-line{position:absolute;left:424px;width:276px;height:2px;background:#222}
  .zip-boxes{position:absolute;left:518px;top:432px;display:flex;border:1.5px solid #222}
  .zip-boxes span{width:30px;height:30px;border-right:1.5px solid #222}
  .zip-boxes span:last-child{border-right:none}
</style>
</head>
<body>

<section class="card front" aria-label="Postcard front">
  <svg class="front-band" viewBox="0 0 730 492" preserveAspectRatio="none" aria-hidden="true">
    <polygon points="450,160 560,40 700,180 590,300" fill="#ffffff" opacity=".04"/>
    <polygon points="180,330 300,220 430,340 310,460" fill="#ffffff" opacity=".04"/>
    <polygon points="0,0 730,0 730,84 478,84 446,128 0,128" fill="var(--band)"/>
    <polyline points="0,130 448,130 480,86 730,86" fill="none" stroke="var(--gold)" stroke-width="5"/>
  </svg>

  <h1 class="title title-1">THE LAW OFFICE OF</h1>
  <p class="title title-2">DANIEL R. CASTELLAN</p>
  <p class="subtitle">PITTSBURGH CRIMINAL DEFENSE-PERSONAL INJURY ATTORNEY</p>
  <p class="appointment">SCHEDULE AN APPOINTMENT</p>
  <p class="phone">412-555-0147</p>

  <ul class="features">
    <li class="feature">OVER 20 YEARS' EXPERIENCE ON
      <ul class="practice">
        <li>DUI Defence</li>
        <li>Personal Injury</li>
        <li>Criminal Defence</li>
        <li>Traffic Citations/ License Issues</li>
        <li>Appeals/ Post-Conviction</li>
      </ul>
    </li>
    <li class="feature">REASONABLE FEES IN BOTH CRIMINAL AND CIVIL CASES</li>
    <li class="feature">EXTENSIVE EXPERIENCE WITH A PROVEN RECORD OF SUCCESS</li>
    <li class="feature">SOME OF HIS NOTABLE APPEALS
      <ul class="appeals">
        <li>United States v. Harlow, 277 F.3d 426 (3rd Cir. 2002)</li>
        <li>Commonwealth v. Dorsey , 927 A.2d 279 (Pa.Super. 2007)</li>
        <li>Commonwealth v. Pell, 909 A.2d 805 (Pa.Super 2006)</li>
        <li>Varga v. Pennsylvania Board of Probation and Parole ,757 A.2d 439<br>(Pa.Cmwlth 2000)</li>
        <li>Commonwealth v. Varga, 710 A.2d 1213 (Pa.Super. 1997)</li>
        <li>Commonwealth v. Brandt, 545 Pa. 487, 681 A.2d 1288 (1995)</li>
        <li>Commonwealth v. Ketter, 545 Pa. 4, 679 A.2d 756 (1993</li>
      </ul>
    </li>
  </ul>

  <svg class="photo-cluster" viewBox="612 162 206 236" role="img" aria-label="Four diamond-shaped photos: scales of justice with gavel, a person with an injured arm, the attorney in shirt and tie, and a damaged car">
    <defs>
      <linearGradient id="warm" x1="0" y1="0" x2="1" y2="1"><stop offset="0" stop-color="#e9d2b8"/><stop offset="1" stop-color="#8a5a35"/></linearGradient>
      <linearGradient id="pale" x1="0" y1="0" x2="1" y2="1"><stop offset="0" stop-color="#f1ece8"/><stop offset="1" stop-color="#b89a8c"/></linearGradient>
      <linearGradient id="office" x1="0" y1="0" x2="1" y2="1"><stop offset="0" stop-color="#c9ccd2"/><stop offset="1" stop-color="#7c8591"/></linearGradient>
      <linearGradient id="steel" x1="0" y1="0" x2="1" y2="1"><stop offset="0" stop-color="#d3d7dc"/><stop offset="1" stop-color="#4c5560"/></linearGradient>
    </defs>
    <g stroke="#ffffff" stroke-width="4">
      <polygon points="728,164 780,216 728,268 676,216" fill="url(#warm)"/>
      <polygon points="668,222 722,276 668,330 614,276" fill="url(#pale)"/>
      <polygon points="786,222 818,254 818,302 786,334 732,278" fill="url(#office)"/>
      <polygon points="728,282 786,340 728,396 670,340" fill="url(#steel)"/>
    </g>
  </svg>
</section>

<section class="card back" aria-label="Postcard back">
  <div class="back-panel">
    <p class="pill pill-map">LOCATON MAP</p>
    <div class="map" role="img" aria-label="Street map of downtown Pittsburgh with a pin marking the law office"></div>
    <p class="pill pill-contact">CONTACT INFO.</p>
    <address class="contact contact-address">
      <span class="name">DANIEL R. CASTELLAN</span><br>
      1800 Counsel Building<br>
      512 Grant Street<br>
      Pittsburgh, PA 15222<br>
      Pennsylvania, U.S.A
    </address>
    <p class="contact contact-lines">
      TEL: 412-555-0147<br>
      <span class="indent-phone">412-555-0192</span><br>
      FAX: 412-555-0168<br>
      E-Mail: dan@drc-law.net<br>
      <span class="indent-mail">dcastel@tovacounsel.net</span>
    </p>
    <p class="websites">www.brookvaledefenselaw.com<br>www.tovacounsel.net.</p>
  </div>

  <div class="stamp">STAMP</div>
  <div class="address-line" style="top:238px"></div>
  <div class="address-line" style="top:276px"></div>
  <div class="address-line" style="top:314px"></div>
  <div class="address-line" style="top:355px"></div>
  <div class="zip-boxes" aria-hidden="true"><span></span><span></span><span></span><span></span><span></span><span></span></div>
</section>

</body>
</html>
```